massage therapy Business Card Design

massage therapy business card
I would like a custom logo created as well.
My vision is angel wings with the HB business initials in between them.
A very simple design.
Colors preferred are light blues and greens.

Target Market(s)

Massage, Spa, fitness

Industry/Entity Type

Massage Therapy

Contact Information for Business Card

A Harbor Breeze
Nora Campe
Massage Therapist and Veldane Pulse Method Practitioner
2870 Marlow Ridge Road, Conway, AR 72039
501-384-6190
nora.harborbreeze@mailvinto.com

Colors
abd036
33a6d7
3176b5
0255a3
0392cd
9bcb3c
cadf82

Requirements
Must have
• the logo must have angel wing.

```html
<!DOCTYPE html>
<html lang="en">
<head>
<meta charset="utf-8">
<title>A Harbor Breeze – Business Card</title>
<link rel="stylesheet" href="https://fonts.googleapis.com/css2?family=Open+Sans:wght@400;600&display=swap">
<style>
  :root {
    --stage: #eef1f4;
    --card-blue-top: #1c98e8;
    --card-blue-bottom: #0a7cd2;
    --brand-blue: #1a86d8;
    --ink: #2a2a2a;
    --white: #ffffff;
    --shadow: rgba(20, 40, 60, 0.18);
  }
  * { box-sizing: border-box; margin: 0; padding: 0; }
  html, body {
    width: 1200px;
    height: 900px;
    overflow: hidden;
    background: var(--stage);
    font-family: "Open Sans", Arial, sans-serif;
  }
  .stage {
    position: relative;
    width: 1200px;
    height: 900px;
  }
  .card {
    position: absolute;
    left: 320px;
    width: 560px;
    height: 320px;
    border-radius: 4px;
    box-shadow: 0 10px 30px var(--shadow);
    overflow: hidden;
  }
  .card--front {
    top: 110px;
    background: linear-gradient(180deg, var(--card-blue-top), var(--card-blue-bottom));
    display: flex;
    flex-direction: column;
    align-items: center;
    justify-content: center;
    gap: 18px;
  }
  .card--back {
    top: 470px;
    background: var(--white);
  }
  .brand-dot {
    width: 66px;
    height: 66px;
    border-radius: 50%;
  }
  .card--front .brand-dot { background: var(--white); }
  .card--front .brand-name {
    color: var(--white);
    font-size: 40px;
    font-weight: 400;
    letter-spacing: 0.5px;
  }
  .back-brand {
    position: absolute;
    left: 20px;
    top: 40px;
    width: 240px;
    display: flex;
    flex-direction: column;
    align-items: center;
    gap: 12px;
  }
  .card--back .brand-dot {
    width: 50px;
    height: 50px;
    background: var(--brand-blue);
  }
  .card--back .brand-name {
    color: var(--brand-blue);
    font-size: 26px;
    font-weight: 400;
    white-space: nowrap;
  }
  .contact {
    position: absolute;
    left: 276px;
    top: 40px;
    width: 264px;
    color: var(--ink);
    font-size: 13px;
    line-height: 1.4;
  }
  .contact__name {
    color: var(--brand-blue);
    font-size: 20px;
    font-weight: 600;
    margin-bottom: 2px;
  }
  .contact__title { margin-left: 10px; margin-bottom: 22px; }
  .contact__address { margin-left: 26px; font-style: normal; margin-bottom: 16px; }
  .contact__line {
    display: flex;
    align-items: center;
    gap: 7px;
    margin-left: 34px;
    font-size: 12px;
    white-space: nowrap;
  }
  .contact__line svg { flex: none; fill: var(--brand-blue); }
</style>
</head>
<body>
<main class="stage">
  <section class="card card--front" aria-label="Card front">
    <span class="brand-dot" aria-hidden="true"></span>
    <span class="brand-name">A Harbor Breeze</span>
  </section>

  <section class="card card--back" aria-label="Card back">
    <div class="back-brand">
      <span class="brand-dot" aria-hidden="true"></span>
      <span class="brand-name">A Harbor Breeze</span>
    </div>
    <div class="contact">
      <h1 class="contact__name">Nora Campe</h1>
      <p class="contact__title">Massage Therapist and Veldane<br>Pulse Method Practitioner</p>
      <address class="contact__address">2870 Marlow Ridge Road,<br>Conway, AR 72039</address>
      <p class="contact__line">
        <svg width="12" height="12" viewBox="0 0 24 24" aria-hidden="true"><path d="M6.6 10.8a15.1 15.1 0 0 0 6.6 6.6l2.2-2.2c.3-.3.7-.4 1-.2 1.1.4 2.3.6 3.6.6.6 0 1 .4 1 1V20c0 .6-.4 1-1 1A17 17 0 0 1 3 4c0-.6.4-1 1-1h3.5c.6 0 1 .4 1 1 0 1.3.2 2.5.6 3.6.1.3 0 .7-.2 1z"/></svg>
        501-384-6190
      </p>
      <p class="contact__line">
        <svg width="12" height="10" viewBox="0 0 24 18" aria-hidden="true"><path d="M0 0h24v18H0z M2 2v1l10 7 10-7V2z" fill-rule="evenodd"/></svg>
        nora.harborbreeze@mailvinto.com
      </p>
    </div>
  </section>
</main>
</body>
</html>
```